one page cv update

I need you to make my one page cv look professional . Needs tidying
Updates

Please note I want the one page CV as close to the original design as possible. Thanks

Colors
00AB8E
00BBA5
67D7C9
C6EFE9
E9F9F6

Requirements
Must have
• Must look as close as possible to original

```html
<!DOCTYPE html>
<html lang="en">
<head>
<meta charset="utf-8">
<title>One Page CV</title>
<link rel="stylesheet" href="https://fonts.googleapis.com/css2?family=Poppins:wght@400;600&display=swap">
<style>
  :root{
    --teal-deep:#00AB8E;
    --teal:#00BBA5;
    --teal-mid:#67D7C9;
    --teal-soft:#C6EFE9;
    --teal-mist:#E9F9F6;
    --ink:#1f2a2e;
    --text:#33393c;
    --paper:#ffffff;
  }
  *{box-sizing:border-box;margin:0;padding:0}
  html,body{width:849px;height:1200px;overflow:hidden;background:var(--paper)}
  body{font-family:'Poppins',Arial,sans-serif;color:var(--text)}
  .cv{position:relative;width:849px;height:1200px;overflow:hidden;background:var(--paper)}

  .texture{position:absolute}
  .texture--top{left:0;top:0;width:260px;height:240px;
    background:radial-gradient(ellipse at 30% 25%,var(--teal-mist) 0%,rgba(233,249,246,0.5) 55%,rgba(255,255,255,0) 80%)}
  .texture--bottom{right:0;bottom:0;width:300px;height:320px;
    background:radial-gradient(ellipse at 75% 75%,var(--teal-mist) 0%,rgba(233,249,246,0.5) 55%,rgba(255,255,255,0) 80%)}

  .header-band{position:absolute;left:0;top:115px;width:640px;height:60px;background:var(--teal-soft)}

  .portrait{position:absolute;left:592px;top:6px;width:172px;height:172px;border-radius:50%;
    border:7px solid var(--teal-soft);
    background:radial-gradient(circle at 50% 40%,#b9b2ad 0%,#6f6560 55%,#3e3a3a 100%)}

  .section{position:absolute}
  .section h2{font-size:15px;font-weight:600;color:var(--ink);padding-bottom:8px;
    border-bottom:1.5px solid var(--teal-mid);margin-bottom:14px}
  .section ul{list-style:none}
  .section li{font-size:11.5px;line-height:1.55;margin-bottom:5px;position:relative;padding-left:10px}
  .section li::before{content:"•";position:absolute;left:0}

  .expertise{left:42px;top:478px;width:300px}
  .industries{left:42px;top:778px;width:300px}
  .industries li{margin-bottom:14px;padding-left:22px}
  .industries li::before{left:10px}
  .qualifications{left:458px;top:478px;width:300px}
  .voluntary{left:458px;top:732px;width:300px}
  .voluntary li{margin-bottom:8px}
  .honours{left:458px;top:940px;width:300px}

  .contact{position:absolute;left:42px;top:1088px;width:300px}
  .contact h3{font-size:11.5px;font-weight:600;color:var(--ink);padding-bottom:6px;
    border-bottom:1.5px solid var(--teal-mid);margin-bottom:10px}
  .contact-row{display:flex;align-items:center;gap:12px;font-size:11.5px;margin-bottom:8px}
  .contact-row svg{width:16px;height:16px;flex:none}
</style>
</head>
<body>
<main class="cv">
  <div class="texture texture--top" role="img" aria-label="Faint hexagon pattern in pale teal"></div>
  <div class="texture texture--bottom" role="img" aria-label="Faint hexagon pattern in pale teal"></div>

  <div class="header-band"></div>
  <div class="portrait" role="img" aria-label="Portrait photograph of the CV owner"></div>

  <section class="section expertise">
    <h2>Expertise</h2>
    <ul>
      <li>Leading organisational transformation</li>
      <li>Governance and risk</li>
      <li>ESG and Diversity and Inclusion</li>
      <li>Crisis management and disaster response</li>
      <li>Diplomacy, negotiation, and mediation</li>
      <li>Public speaking</li>
      <li>Public Private Partnerships that deliver shared value for business and community</li>
      <li>Papua New Guinea and Pacific</li>
    </ul>
  </section>

  <section class="section industries">
    <h2>Industries and sectors</h2>
    <ul>
      <li>Government</li>
      <li>Private Sector ESG</li>
      <li>International and Regional Affairs</li>
      <li>Philanthropy</li>
      <li>Domestic and Family Violence Services</li>
    </ul>
  </section>

  <section class="section qualifications">
    <h2>Qualifications</h2>
    <ul>
      <li>Master Social Work, University of Southbank (2025)</li>
      <li>IGCD (2014) • Master of Philosophy, University of Fenwick (1993)</li>
      <li>BA Political Science University of Westmoor (1990)</li>
      <li>Nationally Accredited Mediator (2022)</li>
    </ul>
  </section>

  <section class="section voluntary">
    <h2>Voluntary roles</h2>
    <ul>
      <li>Board Director Kindred PNG (2014-current)</li>
      <li>Board Director Bridgeway Foundation (current)</li>
      <li>Volunteer Capital Wildlife (current)</li>
      <li>Volunteer Comfort Care Australia (current)</li>
      <li>Board Director ChildAid Australia (Past)</li>
    </ul>
  </section>

  <section class="section honours">
    <h2>Australian Honours</h2>
    <ul>
      <li>Member of the Order of Australia (2021) for contribution to social development in PNG.</li>
    </ul>
  </section>

  <section class="contact">
    <h3>Contact information</h3>
    <div class="contact-row">
      <svg viewBox="0 0 24 24" aria-hidden="true"><path fill="#1f2a2e" d="M6.6 10.8a15.1 15.1 0 0 0 6.6 6.6l2.2-2.2a1 1 0 0 1 1-.25 11.4 11.4 0 0 0 3.6.57 1 1 0 0 1 1 1V20a1 1 0 0 1-1 1A17 17 0 0 1 3 4a1 1 0 0 1 1-1h3.5a1 1 0 0 1 1 1c0 1.25.2 2.45.57 3.57a1 1 0 0 1-.25 1z"/></svg>
      <span>+61400555021</span>
    </div>
    <div class="contact-row">
      <svg viewBox="0 0 24 24" aria-hidden="true"><rect x="2" y="5" width="20" height="14" rx="1.5" fill="none" stroke="#d9453b" stroke-width="2"/><path d="M3 6l9 7 9-7" fill="none" stroke="#d9453b" stroke-width="2"/></svg>
      <span>s.hartwell@mailhub.com</span>
    </div>
  </section>
</main>
</body>
</html>
```